Tovrel Business Card

We are a modern retail clothing store. Established in 1994. I need a presentable card that will amaze vendors when given to them.

Front: Logo in middle
Info Side:

Name: Omar Latif
Cell: 630-555-0148
Work: 630-555-0192 EXT. 230
Email: Omar@tovrel.example
Website: www.Tovrel.example

Industry/Entity Type

Business

```html
<!DOCTYPE html>
<html lang="en">
<head>
<meta charset="utf-8">
<title>Tovrel Business Card</title>
<link rel="stylesheet" href="https://fonts.googleapis.com/css2?family=Exo+2:wght@600;700&family=Roboto:wght@400;500&display=swap">
<style>
  :root {
    --backdrop: #a9a7a7;
    --card-dark: #1b1b1b;
    --card-light: #f1f1f1;
    --ink: #1d1d1d;
    --ink-soft: #333333;
    --rule: #8a8a8a;
    --band-grey: #6e6d6d;
    --paper-white: #ffffff;
  }
  * { margin: 0; padding: 0; box-sizing: border-box; }
  html, body {
    width: 1200px; height: 1200px; overflow: hidden;
    background: var(--backdrop);
  }
  .canvas { position: relative; width: 1200px; height: 1200px; }

  .card {
    position: absolute;
    border-radius: 24px;
    overflow: hidden;
  }
  .card-front {
    left: 238px; top: 117px; width: 712px; height: 420px;
    background: var(--card-dark);
    display: flex; align-items: center; justify-content: center;
  }
  .wordmark {
    font-family: "Exo 2", sans-serif;
    font-weight: 700;
    letter-spacing: 2px;
    line-height: 1;
  }
  .card-front .wordmark {
    color: var(--paper-white);
    font-size: 96px;
    margin-top: -10px;
  }

  .card-back {
    left: 232px; top: 645px; width: 711px; height: 415px;
    background: var(--card-light);
  }
  .card-back .wordmark {
    position: absolute; left: 36px; top: 76px;
    color: var(--ink);
    font-size: 80px;
  }
  .identity {
    position: absolute; right: 35px; top: 206px;
    text-align: right;
  }
  .person-name {
    font-family: "Exo 2", sans-serif;
    font-weight: 700;
    font-size: 27px;
    color: var(--ink);
    letter-spacing: 0.5px;
  }
  .person-role {
    font-family: "Roboto", sans-serif;
    font-size: 16px;
    color: var(--ink-soft);
    margin-top: 2px;
  }
  .divider {
    position: absolute; left: 36px; top: 257px;
    width: 482px; height: 1px; background: var(--rule);
  }
  .contacts {
    position: absolute; left: 36px; top: 284px;
    list-style: none;
    font-family: "Roboto", sans-serif;
    font-size: 18px;
    color: var(--ink);
  }
  .contacts li {
    display: flex; align-items: center;
    height: 26px;
  }
  .contacts svg { width: 16px; height: 16px; margin-right: 19px; fill: var(--ink); }
  .website {
    position: absolute; right: 42px; top: 325px;
    font-family: "Roboto", sans-serif;
    font-weight: 500;
    font-size: 17px;
    color: var(--ink);
    letter-spacing: 0.5px;
  }
  .footer-bands {
    position: absolute; left: 0; bottom: 0; width: 711px; height: 44px;
  }
</style>
</head>
<body>
<div class="canvas">

  <section class="card card-front" aria-label="Card front">
    <span class="wordmark">TOVREL</span>
  </section>

  <section class="card card-back" aria-label="Card back">
    <span class="wordmark">TOVREL</span>

    <div class="identity">
      <div class="person-name">Omar Latif</div>
      <div class="person-role">Managing Director</div>
    </div>

    <div class="divider"></div>

    <ul class="contacts">
      <li>
        <svg viewBox="0 0 16 16" aria-hidden="true"><path d="M4 0h8a1 1 0 0 1 1 1v14a1 1 0 0 1-1 1H4a1 1 0 0 1-1-1V1a1 1 0 0 1 1-1zm1 2v10h6V2zm3 11a1 1 0 1 0 0 2 1 1 0 0 0 0-2z"/></svg>
        630-555-0148
      </li>
      <li>
        <svg viewBox="0 0 16 16" aria-hidden="true"><path d="M1 5c0-2 3-3 7-3s7 1 7 3v1h-4V5H5v1H1zm2 2h10l2 7H1zm5 1.5a2.5 2.5 0 1 0 0 5 2.5 2.5 0 0 0 0-5z"/></svg>
        630-555-0192 EXT. 230
      </li>
      <li>
        <svg viewBox="0 0 16 16" aria-hidden="true"><path d="M1 3h14v10H1zm1.5 1.3V12h11V4.3L8 8.6z M3 4l5 3.8L13 4z"/></svg>
        Omar@tovrel.example
      </li>
    </ul>

    <div class="website">www.Tovrel.example</div>

    <svg class="footer-bands" viewBox="0 0 711 44" aria-hidden="true">
      <rect x="0" y="24" width="420" height="20" fill="var(--band-grey)"/>
      <polygon points="398,4 711,4 711,44 375,44" fill="var(--card-dark)"/>
    </svg>
  </section>

</div>
</body>
</html>
```